Financial planning wealth advisor Business Card

We have a finanancial advisory that caters to high net worth and business owner clients. We would like a card that works with our entire style. Please visit out website brightharborplanning.com to get a look and feel.... VERY OPEN to interesting and unique designs that have cutouts, fold overs, anything to capture interest...

Requirements, info must be the following:

Harbor Light Planning (with Logo)
Investments | Insurance | Retirement | Education | Estate | Business Planning

Nora Valk Penhallow, CFP, MSFS, AEP
Principal

915-720-5814 (Main)
915-286-9051 (Cell)
epenhallow@brightharborplanning.com

Central Location:
518 W Marlowe Suite 740
El Paso TX 79935

West Location:
2613 Thistlegate Lane SuiteB
El Paso TX 79948

brightharborplanning.com

DISCLOSURES (Back of Card)
Eleanor Valk Penhallow, CFP, MSFS, AEP, a Registered Representative offering securities through QUILLMARK Brokerage LLC. 518 W Marlowe Suite 740 El Paso TX 79935 915-867-2409. Member BRAVEN/TOLLIC, a licensed insurance agency.

*Financial Adviser offering investment advisory services through Juniper Advisory, LLC, a Registered Investment Advisor.

Harbor Light Planning is not owned or operated by QUILLMARK Brokerage LLC or its affiliates.

Target Market(s)

High end affluent or ultra rich clientele

Industry/Entity Type

Financial Planning

Font styles to use
Decorative

Requirements
Must have
• Needs to have something that focuses our services. :33 bellow for our original business card.

```html
<!DOCTYPE html>
<html lang="en">
<head>
<meta charset="utf-8">
<title>Harbor Light Planning – Business Card</title>
<link href="https://fonts.googleapis.com/css2?family=Montserrat:wght@400;500;600;700&display=swap" rel="stylesheet">
<style>
  :root {
    --bg: #2b2b2d;
    --gold: #d4b06a;
    --gold-deep: #c9a55e;
    --gold-text: #d9b46a;
    --ink: #1a1a1a;
    --black: #050505;
    --white: #ffffff;
  }
  * { box-sizing: border-box; margin: 0; padding: 0; }
  html, body { width: 1200px; height: 900px; overflow: hidden; }
  body {
    background: var(--bg);
    font-family: "Montserrat", Arial, sans-serif;
    position: relative;
  }
  .card {
    position: absolute;
    width: 640px;
    height: 366px;
    overflow: hidden;
    box-shadow: 0 10px 30px rgba(0,0,0,.45);
  }

  /* Back of card – disclosures */
  .card-back {
    left: 120px;
    top: 60px;
    background: var(--gold);
    color: var(--ink);
    text-align: center;
  }
  .card-back .arrow-motif {
    position: absolute;
    inset: 0;
    background: radial-gradient(ellipse at 50% 85%, rgba(255,255,255,.28), rgba(255,255,255,0) 65%);
  }
  .card-back .disclosure {
    position: relative;
    padding-top: 62px;
    font-size: 17px;
    line-height: 1.3;
  }
  .card-back .holder { font-size: 18px; }
  .card-back .holder-name { color: var(--white); font-weight: 700; }
  .card-back .small { font-size: 14px; }
  .card-back .services {
    margin-top: 12px;
    font-size: 17px;
    letter-spacing: .02em;
  }

  /* Front of card */
  .card-front {
    left: 460px;
    top: 474px;
    display: flex;
    background: var(--black);
  }
  .brand-panel {
    width: 250px;
    background: var(--white);
    border-right: 5px solid var(--gold-deep);
    display: flex;
    align-items: center;
    justify-content: center;
  }
  .brand-name {
    font-size: 24px;
    font-weight: 600;
    color: var(--ink);
    text-align: center;
    line-height: 1.2;
    letter-spacing: .04em;
  }
  .contact-panel {
    flex: 1;
    padding: 34px 30px 0 38px;
    color: var(--white);
    font-size: 16px;
    line-height: 1.25;
  }
  .contact-panel .person-name {
    color: var(--gold-text);
    font-size: 22px;
    font-weight: 600;
  }
  .contact-panel .credentials { font-size: 21px; }
  .contact-panel .role { font-size: 13px; margin-bottom: 4px; }
  .contact-panel .label { color: var(--gold-text); font-weight: 600; }
  .contact-panel .address { margin-bottom: 2px; }
  .contact-list { list-style: none; margin-top: 18px; }
  .contact-list li { display: flex; align-items: center; gap: 10px; font-size: 15px; }
  .contact-list svg { width: 12px; height: 12px; fill: var(--gold-text); flex: none; }
</style>
</head>
<body>

<section class="card card-back">
  <div class="arrow-motif" role="img" aria-label="Faint rising arrows decoration"></div>
  <div class="disclosure">
    <p class="holder"><span class="holder-name">Eleanor Valk Penhallow -</span> CFP, MSFS, AEP,</p>
    <p class="small">Member</p>
    <p class="small">P: 915-867-2409</p>
    <p>A Registered Representative</p>
    <p>Offering securities through QUILLMARK Brokerage LLC.</p>
    <p class="services">INVESTMENTS | INSURANCE | RETIREMENT<br>EDUCATION | ESTATE | BUSINESS PLANNING</p>
  </div>
</section>

<section class="card card-front">
  <div class="brand-panel">
    <p class="brand-name">HARBOR LIGHT<br>PLANNING</p>
  </div>
  <div class="contact-panel">
    <p class="person-name">Nora Valk Penhallow</p>
    <p class="credentials">(CFP, MSFS, AEP)</p>
    <p class="role">Principal</p>
    <p class="label">Central Location:</p>
    <p class="address">518 W Marlowe Suite 740<br>El Paso TX 79935</p>
    <p class="label">West Location:</p>
    <p class="address">2613 Thistlegate Lane SuiteB<br>El Paso TX 79948</p>
    <ul class="contact-list">
      <li><svg viewBox="0 0 12 12"><path d="M2 1h2.5l1 3-1.5 1a6 6 0 0 0 3 3l1-1.5 3 1V10a1 1 0 0 1-1 1A9 9 0 0 1 1 2a1 1 0 0 1 1-1z"/></svg>915-720-5814</li>
      <li><svg viewBox="0 0 12 12"><path d="M3 0h6a1 1 0 0 1 1 1v10a1 1 0 0 1-1 1H3a1 1 0 0 1-1-1V1a1 1 0 0 1 1-1zm0 2v7h6V2zm3 8a.6.6 0 1 0 0 1.2.6.6 0 0 0 0-1.2z"/></svg>915-286-9051</li>
      <li><svg viewBox="0 0 12 12"><path d="M0 2h12v8H0zm1 1v.3l5 3.2 5-3.2V3zm0 1.5V9h10V4.5L6 7.7z"/></svg>epenhallow@brightharborplanning.com</li>
      <li><svg viewBox="0 0 12 12"><path d="M6 0a6 6 0 1 0 0 12A6 6 0 0 0 6 0zm0 1c.8 0 1.6 1.8 1.8 4.5H4.2C4.4 2.8 5.2 1 6 1zM1 6.5h2.2c.1 1.7.4 3 .9 4A5 5 0 0 1 1 6.5zm0-1A5 5 0 0 1 4.1 1.5c-.5 1-.8 2.3-.9 4zm5 5.5c-.8 0-1.6-1.8-1.8-4.5h3.6C7.6 9.2 6.8 11 6 11zm1.9-.5c.5-1 .8-2.3.9-4H11a5 5 0 0 1-3.1 4zM8.8 5.5c-.1-1.7-.4-3-.9-4A5 5 0 0 1 11 5.5z"/></svg>www.brightharborplanning.com</li>
    </ul>
  </div>
</section>

</body>
</html>
```